Card for invoking rights with police

Our criminal defense law firm is seeking proposals for a design for our card intended for clients to carry with them in their car. Upon being pulled over, they would hand this card to the officer.
Text for the back of the card:
"For Law Enforcement:"
"I will comply with lawful orders but respectfully decline any test or other requests without my attorney. I wish to remain silent, do not consent to searches, and request to speak with my attorney now.
The back of the card should prominently feature the text and the firm logo should be secondary.
Front
Must prominently feature contact info: 503-555-0182. Do not include attorney name, email, phone from the example file. This is intended to be generic for the firm and not tied to an individual lawyer.
Included for design reference: current business card, firm logo.
We intend to use trenvo.com to produce the cards.
Updates
The back of the card should prominently display the text regarding invocation of rights. Please title it "For Law Enforcement".
Target Market(s)
People who have been stopped by police
Contact Information for Business Card
see project description
Look and feel

```html
<!DOCTYPE html>
<html lang="en">
<head>
<meta charset="utf-8">
<title>Halvorsen Law Firm – Rights Card</title>
<link rel="stylesheet" href="https://fonts.googleapis.com/css2?family=Lato:wght@400;700;900&display=swap">
<style>
  :root {
    --navy: #0c3558;
    --white: #ffffff;
    --ink-grey: #5a5f66;
    --pale: #eef0f3;
    --stage: #2a2c30;
    --body-font: "Lato", sans-serif;
  }
  * { box-sizing: border-box; margin: 0; padding: 0; }
  html, body { width: 1200px; height: 952px; overflow: hidden; }
  body {
    background: var(--stage);
    font-family: var(--body-font);
    display: flex;
    align-items: center;
    justify-content: center;
    gap: 60px;
  }
  .card {
    position: relative;
    width: 520px;
    height: 297px;
    border-radius: 18px;
    overflow: hidden;
    background: var(--white);
    box-shadow: 0 10px 28px rgba(0,0,0,.45);
  }

  /* Firm name lockup */
  .firm-name {
    display: flex;
    align-items: center;
    gap: 12px;
    color: var(--navy);
    font-weight: 700;
  }
  .firm-name .mark { display: block; background: var(--navy); }
  .firm-name .words { letter-spacing: .18em; line-height: 1.1; }

  /* Back card: invocation of rights */
  .rights-card .firm-name {
    position: absolute;
    top: 42px;
    left: 0; right: 0;
    justify-content: center;
    font-size: 24px;
  }
  .rights-card .firm-name .mark { width: 34px; height: 34px; }
  .rights-panel {
    position: absolute;
    left: 0; right: 0; bottom: 0;
    height: 170px;
    background: var(--navy);
    color: var(--white);
    text-align: center;
    padding: 0 34px;
  }
  .rights-title {
    display: inline-block;
    margin-top: -16px;
    padding: 5px 18px;
    background: var(--navy);
    border: 2px solid var(--white);
    border-radius: 16px;
    font-weight: 900;
    font-size: 17px;
  }
  .rights-text {
    margin-top: 16px;
    font-size: 14.5px;
    line-height: 1.55;
  }

  /* Front card: firm contact */
  .contact-card .firm-name {
    position: absolute;
    top: 24px;
    left: 30px;
    font-size: 20px;
  }
  .contact-card .firm-name .mark { width: 28px; height: 28px; }
  .address-line {
    position: absolute;
    left: 30px;
    top: 78px;
    display: flex;
    gap: 8px;
    font-size: 12px;
    line-height: 1.3;
    color: var(--ink-grey);
  }
  .address-line svg { width: 14px; height: 14px; flex: 0 0 14px; }
  .contact-band {
    position: absolute;
    left: 0;
    top: 118px;
    width: 300px;
    height: 124px;
    background: var(--navy);
    color: var(--white);
    padding: 22px 0 0 30px;
    list-style: none;
  }
  .contact-band li {
    display: flex;
    align-items: center;
    gap: 10px;
    line-height: 1.3;
  }
  .contact-band svg { flex: 0 0 auto; }
  .contact-phone { font-size: 24px; font-weight: 900; letter-spacing: .02em; margin-bottom: 16px; }
  .contact-phone svg { width: 22px; height: 22px; }
  .contact-web { font-size: 14px; }
  .contact-web svg { width: 15px; height: 15px; }
  .pale-strip {
    position: absolute;
    left: 300px; right: 0;
    top: 242px; bottom: 0;
    background: var(--pale);
  }
</style>
</head>
<body>

  <section class="card rights-card" aria-label="Back of card: for law enforcement">
    <div class="firm-name"><span class="mark"></span><span class="words">HALVORSEN<br>LAW FIRM</span></div>
    <div class="rights-panel">
      <h2 class="rights-title">For Law Enforcement:</h2>
      <p class="rights-text">I will comply with lawful orders but respectfully decline any test or other requests without my attorney. I wish to remain silent, do not consent to searches, and request to speak with my attorney now.</p>
    </div>
  </section>

  <section class="card contact-card" aria-label="Front of card: firm contact details">
    <div class="firm-name"><span class="mark"></span><span class="words">HALVORSEN<br>LAW FIRM</span></div>
    <p class="address-line">
      <svg viewBox="0 0 14 14" aria-hidden="true"><rect width="14" height="14" rx="2" fill="#0c3558"/><path d="M7 2.5a3 3 0 0 0-3 3c0 2.2 3 5.5 3 5.5s3-3.3 3-5.5a3 3 0 0 0-3-3z" fill="#fff"/><circle cx="7" cy="5.5" r="1.1" fill="#0c3558"/></svg>
      <span>1250 Harbor Point Ave,<br>Suite 210 Easton, WA 98100</span>
    </p>
    <ul class="contact-band">
      <li class="contact-phone">
        <svg viewBox="0 0 14 14" aria-hidden="true"><rect width="14" height="14" rx="2" fill="#fff"/><path d="M4 3l2 .3.6 2-1 .8a6 6 0 0 0 2.3 2.3l.8-1 2 .6.3 2c-4 .5-7.5-3-7-7z" fill="#0c3558"/></svg>
        <span>503-555-0182</span>
      </li>
      <li class="contact-web">
        <svg viewBox="0 0 14 14" aria-hidden="true"><rect width="14" height="14" rx="2" fill="#fff"/><path d="M4 3l6 4-2.6.6L9 11l-1.2.5-1.5-3.3L4 10z" fill="#0c3558"/></svg>
        <span>www.halvorsenlaw.com</span>
      </li>
    </ul>
    <div class="pale-strip"></div>
  </section>

</body>
</html>
```